Folded Business Cards, Envelopes, Information card and Thank You card.
Gala Tent Company
Folded Business Cards, Envelopes, Information card and Thank You card. - Events
Creative Brief
Modern
Marisol Fenwick-Dutra
Owner-Linen Specialist
2718 Harbor Crest Ave Suite 204B Long Beach CA 90807
marisol@larkspurdrapery.example
larkspurdraperys.example
Our colors are silver, grey, dark plum and eggplant. I would like something modern with maybe translucent floral scrolls in the background. I am open to card back ground color. It can be silver, plum/eggplant or even white. We are a high-end wedding linen rental company. Our clients are mostly female, mid income and are planning a wedding. I am looking for the following items: 1. Business Card. 2. Envelope. 3. Information Card. 4. Thank You Card. Information Card: This is an information card that will be sent out with each order. It will be printed on a 6" x 9" post card one sided. Bellow is the text that will go on the card Important Information Regarding Your Linen Returns. Thank you for allowing Larkspur Drapery linens to share in your special day. To ensure prompt return of your linens, please follow the steps bellow. 1. Please place all linens in the included return duffel bags or the box they arrived in. It returning in a box, please fold linens so that they all fit in the box. Please shake any loose food from linens and insure linens are dry prior to placing in box and bags. NEVER place wet linens in bags, boxes of plastic. If your linens are wet or damp please allow them to air dry prior to packing. If your shipment included chair sashes, please remember to untie each sash prior to return. You account will be billed a fee of $.25 for each sash returned that is untied. 2. If you would like to schedule a ParcelWing pickup, please contact ParcelWing the day PRIOR to your scheduled return date as ParcelWing does not do same pickup. Please note, ParcelWing charges a pickup fee of $8. This fee is paid directly to ParcelWing. You can contact ParcelWing at 1.800.Go.Wing (555-0148). You may also return your linens for free of charge by dropping of your linens at any ParcelWing or ParcelWing Copyhub. Please use the attached pre-paid ParcelWing air-bil that came with your shipment. Lost ParcelWing Air-Bills: Please treat your ParcelWing return air-bills as cash. If they are lost or damaged, please contact us as soon as possible for replacements. We charge a fee of $25 for each lost or damaged air-bill that needs to be replaced. Alternate Shipping Carriers: Your linen rental includes pre-paid return shipping via ParcelWing and include tracking for our warehouse. Please do not return linens using any other shipping provider or any other class of shipping (i.e. Express, Next Day, Over Night these services will be billed back to your account). Late Returns: Our customers depend on your timely return. Please insure our items are dropped off or picked up by ParcelWing the following business day after your event. Items shipped back after the due date are considered late and will be charge a rental fee equal to 50% of your original rental rate prior to any discounts or promotions. Should you have any questions regarding your order please contact our office at 562.555.0173 should you need to reach us after hours or on weekends please leave a message or send an e-mail to afterhours@larkspurdraperys.example. Thank you card: Please also design a matching thank you card that will be printed on a 4" x 6" one sided post card.
Notes: We are using a folded business card: We would like it laid out as follows: Front: Logo with contact details Inside: The inside will have a space where we can glue on a fabric swatch. We would like the swatch to be placed placed in a decorative rectangle that should take up most of the inside. There also needs to be wording under the square that says "Raspberry Satin Back Shantung" we would like this centered. Back: On the back of the card we would like: twitter icon with our twitter id:larkspurcloth youtube logo with our id: larkspurdraperys

```html
<!DOCTYPE html>
<html lang="en">
<head>
<meta charset="utf-8">
<title>Larkspur Drapery Linens – Stationery Set</title>
<link rel="stylesheet" href="https://fonts.googleapis.com/css2?family=Cormorant+Garamond:wght@500&family=Lato:wght@400;700&family=Playfair+Display:ital@1&display=swap">
<style>
  :root{
    --stage:#ebe7e1;
    --paper:#ffffff;
    --silver:#a9a9a9;
    --grey:#8c8c8c;
    --grey-dark:#6b6b6b;
    --ink:#7a7a7a;
    --label:#4a4a4a;
    --flourish-a:rgba(200,200,200,.35);
    --flourish-b:rgba(255,255,255,0);
  }
  *{box-sizing:border-box;margin:0;padding:0}
  html,body{width:1200px;height:943px;overflow:hidden;background:var(--stage)}
  body{position:relative;font-family:'Lato',sans-serif;color:var(--ink)}
  .piece{position:absolute;background:var(--paper);box-shadow:0 2px 6px rgba(0,0,0,.18);overflow:hidden}
  .label{position:absolute;font-size:11px;color:var(--label);font-family:'Lato',sans-serif}
  .flourish{position:absolute;background:radial-gradient(ellipse at center,var(--flourish-a),var(--flourish-b) 70%)}

  /* brand mark */
  .brand{display:flex;flex-direction:column;align-items:center;text-align:center}
  .brand-square{background:var(--silver);display:block}
  .brand-name{font-family:'Cormorant Garamond',serif;font-weight:500;color:var(--grey);letter-spacing:.12em;line-height:1.05;text-transform:uppercase}

  /* thank you inner */
  .ty-inner{left:46px;top:90px;width:313px;height:397px}
  .ty-inner .flourish{left:60px;top:40px;width:240px;height:300px}
  .ty-inner .note{position:absolute;left:26px;bottom:34px;width:190px;font-size:9px;line-height:1.45;color:var(--grey)}

  /* thank you outer */
  .ty-outer{left:364px;top:90px;width:308px;height:397px}
  .ty-outer .band{position:absolute;left:0;top:0;width:100%;height:158px;background:var(--grey)}
  .ty-outer .contacts{position:absolute;left:92px;top:34px;font-size:9px;line-height:1.7;color:#fff;list-style:none}
  .ty-outer .contacts li::before{content:"";display:inline-block;width:6px;height:6px;border:1px solid #fff;border-radius:50%;margin-right:5px;vertical-align:middle}
  .ty-outer .brand{position:absolute;left:0;right:0;top:205px}
  .ty-outer .brand-square{width:30px;height:30px;margin-bottom:8px}
  .ty-outer .brand-name{font-size:14px}
  .ty-outer .thanks{position:absolute;left:0;right:0;top:300px;text-align:center;font-family:'Playfair Display',serif;font-style:italic;font-size:26px;color:var(--silver)}

  /* envelopes */
  .envelope{left:685px;width:474px;height:220px}
  .env-1{top:97px}
  .env-2{top:333px}
  .envelope .flourish{right:30px;top:0;width:260px;height:220px}
  .envelope .brand{position:absolute;left:30px;top:22px;width:90px}
  .envelope .brand-square{width:34px;height:34px;margin-bottom:6px}
  .envelope .brand-name{font-size:11px}
  .envelope .return{position:absolute;left:22px;font-size:7.5px;color:var(--grey-dark)}
  .env-1 .return{top:104px}
  .env-2 .return{top:105px}

  /* info card */
  .info{left:103px;top:500px;width:582px;height:359px}
  .info .flourish{left:300px;top:0;width:280px;height:200px}
  .info .brand{position:absolute;left:24px;top:18px;width:110px}
  .info .brand-square{width:34px;height:34px;margin-bottom:6px}
  .info .brand-name{font-size:14px}
  .info h1{position:absolute;right:22px;top:26px;width:300px;text-align:right;font-size:14px;font-weight:700;line-height:1.3;color:var(--silver)}
  .info .intro{position:absolute;left:24px;top:100px;width:330px;font-size:7.5px;line-height:1.5;color:var(--grey)}
  .info .cols{position:absolute;left:24px;top:140px;right:22px;display:grid;grid-template-columns:1fr 1fr;gap:18px;font-size:5.2px;line-height:1.45;color:var(--grey)}
  .info .cols3{position:absolute;left:24px;top:226px;right:22px;display:grid;grid-template-columns:1fr 1fr 1fr;gap:14px;font-size:5.2px;line-height:1.45;color:var(--grey)}
  .info .cols3 b{display:block;color:var(--grey-dark);margin-bottom:2px}
  .info .footer{position:absolute;left:24px;right:22px;bottom:14px;font-size:5.2px;line-height:1.45;color:var(--grey-dark)}

  /* biz card outer */
  .biz-outer{left:718px;top:636px;width:192px;height:223px}
  .biz-outer .band{position:absolute;left:0;top:0;width:100%;height:80px;background:var(--grey)}
  .biz-outer .social{position:absolute;left:12px;top:12px;transform:rotate(180deg);transform-origin:84px 28px;font-size:6.5px;color:#fff;list-style:none;line-height:1.9}
  .biz-outer .social li::before{content:"";display:inline-block;width:7px;height:7px;background:#fff;border-radius:50%;margin-right:4px;vertical-align:middle}
  .biz-outer .band .brand{position:absolute;right:14px;top:18px;transform:rotate(180deg)}
  .biz-outer .band .brand-name{color:#fff;font-size:10px}
  .biz-outer .front .brand{position:absolute;left:10px;top:128px;width:66px}
  .biz-outer .front .brand-square{width:22px;height:22px;margin-bottom:4px}
  .biz-outer .front .brand-name{font-size:7.5px}
  .biz-outer .details{position:absolute;left:86px;top:94px;font-size:5.6px;line-height:1.55;color:var(--grey-dark)}
  .biz-outer .details strong{display:block;font-size:6.3px}

  /* biz card inner */
  .biz-inner{left:915px;top:636px;width:221px;height:223px}
  .biz-inner .swatch{position:absolute;left:8px;top:8px;width:205px;height:178px;border:2px solid var(--silver);border-radius:10px;background:#fff}
  .biz-inner .caption{position:absolute;left:0;bottom:0;width:100%;height:30px;background:var(--grey);color:#fff;font-size:8.5px;font-weight:700;display:flex;align-items:center;justify-content:center}
</style>
</head>
<body>

<span class="label" style="left:46px;top:72px">Thank you Card Inner</span>
<section class="piece ty-inner">
  <div class="flourish" role="img" aria-label="faint translucent floral scroll"></div>
  <p class="note">Thank you for allowing Larkspur Drapery linens to share in your special day! It was a pleasure working with you and we look forward to working with you in the near future.</p>
</section>

<span class="label" style="left:420px;top:72px">Thank you Card Outer</span>
<section class="piece ty-outer">
  <div class="band">
    <ul class="contacts">
      <li>marisol@larkspurdrapery.example</li>
      <li>larkspurdraperys.example</li>
      <li>562.555.0173</li>
      <li>larkspurcloth</li>
      <li>larkspurdraperys</li>
    </ul>
  </div>
  <div class="brand">
    <span class="brand-square"></span>
    <span class="brand-name">Larkspur<br>Drapery Linens</span>
  </div>
  <p class="thanks">Thank You !</p>
</section>

<section class="piece envelope env-1">
  <div class="flourish" role="img" aria-label="faint translucent floral scroll"></div>
  <div class="brand">
    <span class="brand-square"></span>
    <span class="brand-name">Larkspur<br>Drapery Linens</span>
  </div>
  <p class="return">2718 Harbor Crest Ave, Suite 204B, Long Beach CA 90807</p>
</section>

<section class="piece envelope env-2">
  <div class="flourish" role="img" aria-label="faint translucent floral scroll"></div>
  <p class="return">2718 Harbor Crest Ave, Suite 204B, Long Beach CA 90807</p>
</section>

<section class="piece info">
  <div class="flourish" role="img" aria-label="faint translucent floral scroll"></div>
  <div class="brand">
    <span class="brand-square"></span>
    <span class="brand-name">Larkspur<br>Drapery Linens</span>
  </div>
  <h1>Important Information Regarding<br>Your Linen Returns.</h1>
  <p class="intro">Thank you for allowing Larkspur Drapery linens to share in your special day.<br>To ensure prompt return of your linens, please follow the steps below.</p>
  <div class="cols">
    <p>1. Please place all linens in the included return duffel bags or the box they arrived in. If returning in a box, please fold linens so that they all fit in the box. Please shake any loose food from linens and ensure linens are dry prior to placing in box and bags. NEVER place wet linens in bags, boxes or plastic. If your linens are wet or damp please allow them to air dry prior to packing. If your shipment included chair sashes, please remember to untie each sash prior to return.</p>
    <p>2. If you would like to schedule a ParcelWing pickup, please contact ParcelWing the day PRIOR to your scheduled return date as ParcelWing does not do same day pickup. Please note, ParcelWing charges a pickup fee of $8. You can contact ParcelWing at 1.800.Go.Wing (555-0148). You may also return your linens free of charge by dropping them off at any ParcelWing or ParcelWing Copyhub using the attached pre-paid air-bill.</p>
  </div>
  <div class="cols3">
    <p><b>Lost ParcelWing Air-Bills:</b>Please treat your return air-bills as cash. If they are lost or damaged, please contact us as soon as possible for replacements. We charge a fee of $25 for each air-bill replaced.</p>
    <p><b>Alternate Shipping Carriers:</b>Your rental includes pre-paid return shipping via ParcelWing with tracking. Please do not return linens using any other provider or class of shipping.</p>
    <p><b>Late Returns:</b>Please ensure items are dropped off or picked up the business day after your event. Late items are charged 50% of your original rental rate.</p>
  </div>
  <p class="footer">Should you have any questions regarding your order please contact our office at 562.555.0173. After hours or on weekends please leave a message or e-mail afterhours@larkspurdraperys.example.</p>
</section>

<span class="label" style="left:720px;top:620px">Biz card outer</span>
<section class="piece biz-outer">
  <div class="band">
    <ul class="social">
      <li>larkspurcloth</li>
      <li>larkspurdraperys</li>
    </ul>
    <div class="brand"><span class="brand-name">Larkspur<br>Drapery Linens</span></div>
  </div>
  <div class="front">
    <div class="brand">
      <span class="brand-square"></span>
      <span class="brand-name">Larkspur<br>Drapery Linens</span>
    </div>
    <p class="details"><strong>Marisol Fenwick-Dutra</strong>Owner-Linen Specialist<br>2718 Harbor Crest Ave<br>Suite 204B<br>Long Beach CA 90807<br>562.555.0173<br>marisol@larkspurdrapery.example<br>larkspurdraperys.example</p>
  </div>
</section>

<span class="label" style="left:1040px;top:864px">Biz card Inner</span>
<section class="piece biz-inner">
  <div class="swatch"></div>
  <p class="caption">Raspberry Satin Back Shantung</p>
</section>

</body>
</html>
```